Vantor Reach Unique Marketing Website Design

I am starting a new company that is a thought leader in the marketing consulting space. The company is called Vantor Reach. We intend to build a Wordpress site on the Astra Theme with the Spectra builder. Our goal is to become the leading voice that empowers high-ticket service business leaders to become Vantor Reach by equipping them with the cutting-edge frameworks and decision grade intelligence taught in leading business schools. What we are looking for is a website design that is clean and professional, making some use of white space well also being eye catching and distinctive in the consulting space. We will probably want to have a video on the homepage not in the hero section, but just below to explain the company and what we do. Our tagline is "Be found. Be chosen." I have attached a brand guide with some messaging, our typography choices, and our color system. The full site will have a primary nav that is four pages - About us, Services, Insights (essentially a blog), and Contact Us. The goal of this project is to develop an art direction that I can give to a designer to build loads of new pages.

Target Market(s)

Business owners (mostly male) from 30-60 years old, looking to fix their sales and marketing funnel.

Industry/Entity Type

Marketing consulting

Font styles to use
Sans Serif

Requirements
Must have
• A clean, professional design that builds trust with owners of high-ticket service businesses. We need a space for explainer video, and sections that tell prospects what we do. Would also like to have a blog carousel.
Nice to have
• Social feeds, if possible. See attached documents for colors and fonts.
Should not have
• Our feel is professional enough to be trustworthy, but unique enough to be memorable. Cartoon ideas do not meet the professional test, and we do not want the website to appear feminine.

```html
<!DOCTYPE html>
<html lang="en">
<head>
<meta charset="utf-8">
<title>Vantor Reach – Be Found. Be Chosen.</title>
<link href="https://fonts.googleapis.com/css2?family=Oswald:wght@500;600;700&family=Poppins:ital,wght@0,300;0,400;0,500;0,600;1,300&display=swap" rel="stylesheet">
<style>
:root{
  --blue:#1570e6;
  --blue-top:#2c5fe4;
  --navy:#262f57;
  --hero-navy:#1f2f5a;
  --dark:#2b2b2b;
  --ink:#1d1d1f;
  --text:#4a4a4a;
  --muted:#8a8a8a;
  --light:#f1f2f5;
  --white:#ffffff;
  --star:#17a56b;
}
*{margin:0;padding:0;box-sizing:border-box}
html,body{width:1200px;height:5240px;overflow:hidden}
body{position:relative;background:var(--white);font-family:'Poppins',sans-serif;color:var(--text)}
.abs{position:absolute}
.head{font-family:'Oswald',sans-serif;font-weight:600;color:var(--ink)}
.btn{position:absolute;display:flex;align-items:center;justify-content:center;background:var(--blue);color:var(--white);font-size:12px;font-weight:500;text-decoration:none}
.ph{position:absolute}

/* top bar */
.topbar{position:absolute;left:0;top:0;width:1200px;height:37px;background:var(--blue-top);color:var(--white);font-size:11.5px}
.social-dot{position:absolute;width:13px;height:13px;border:1.6px solid var(--white);border-radius:50%}
.topbar .info{position:absolute;top:11px;display:flex;align-items:center;gap:8px}

/* nav */
.nav{position:absolute;left:0;top:37px;width:1200px;height:85px;background:var(--white)}
.brand{position:absolute;font-family:'Poppins',sans-serif;font-weight:600;color:var(--ink);letter-spacing:-.2px}
.nav .brand{left:160px;top:28px;font-size:23px}
.nav a{position:absolute;top:35px;font-size:12px;color:#333;text-decoration:none}
.nav a.active{color:var(--blue)}

/* hero */
.hero-photo{left:0;top:122px;width:1200px;height:688px;background:linear-gradient(100deg,#1b2a52 0%,#2a3d6e 40%,#51648f 70%,#7d8aa6 100%)}
.hero-title{left:160px;top:276px;font-family:'Oswald',sans-serif;font-weight:700;font-size:100px;line-height:84px;color:var(--white)}
.hero-text{left:161px;top:462px;width:420px;font-size:13.5px;line-height:15px;color:var(--white)}

/* about */
.label{font-size:11.5px;color:var(--ink)}
.about p{position:absolute;left:160px;width:360px;font-size:12.5px;line-height:19px;color:#3a3a3a}

/* help */
.help-card{position:absolute;top:1713px;width:219px;height:243px;background:var(--white);border-radius:4px;padding:30px 18px}
.help-card h3{font-family:'Oswald',sans-serif;font-weight:500;font-size:17px;color:var(--ink);margin-top:18px}
.help-card p{font-size:11px;line-height:13.5px;color:#555;margin-top:10px}
.help-card .more{position:absolute;left:18px;bottom:34px;font-size:10px;color:#333;display:flex;align-items:center;gap:8px}

/* services */
.svc-box{position:absolute;width:380px;height:213px;background:var(--white);padding:30px 36px;box-shadow:0 10px 30px rgba(0,0,0,.08)}
.svc-box h3{font-family:'Oswald',sans-serif;font-weight:500;font-size:21px;color:var(--ink)}
.svc-box p{font-size:12px;line-height:19.5px;color:#555;margin-top:12px}
.svc-box .link{margin-top:6px;font-size:12.5px;color:var(--blue);display:flex;align-items:center;gap:8px}

/* section headings */
.sec-title{position:absolute;left:0;width:1200px;text-align:center;font-family:'Oswald',sans-serif;font-weight:600;font-size:37px;color:var(--ink)}
.sec-sub{position:absolute;left:0;width:1200px;text-align:center;font-size:12.5px;color:#333}

/* reviews */
.review{position:absolute;top:3362px;height:234px;background:var(--white);border:1px solid #e4e4e4;border-radius:8px}
.review .avatar{position:absolute;left:22px;top:44px;width:58px;height:58px;border-radius:50%;background:linear-gradient(135deg,#8d97a8,#3d4558)}
.review .sign{position:absolute;left:100px;top:42px;width:80px;height:30px;background:linear-gradient(90deg,#e6e8ee,#d4d8e0);border-radius:3px}
.review .stars{position:absolute;left:208px;top:42px;font-size:19px;letter-spacing:2px;color:var(--star)}
.review .name{position:absolute;left:100px;top:86px;font-size:13.5px;color:#333}
.review .name b{color:var(--blue);font-weight:600}
.review .quote{position:absolute;right:26px;top:16px;font-family:'Oswald',sans-serif;font-size:120px;line-height:120px;color:#d8d8d8}
.review p{position:absolute;left:100px;top:118px;width:395px;font-size:11.5px;line-height:23px;font-style:italic;font-weight:300;color:#555}

/* team */
.member{position:absolute;top:3863px;width:202px;height:232px;background:linear-gradient(180deg,#e9eaee,#c9ccd3)}
.member .tag{position:absolute;left:16px;top:181px;width:170px;height:75px;background:var(--white);display:flex;align-items:center;justify-content:center;font-weight:600;font-size:13.5px;color:var(--ink);box-shadow:0 6px 18px rgba(0,0,0,.06)}

/* blog */
.post{position:absolute;top:4390px;width:277px;height:325px;background:var(--light);padding:30px 24px}
.post.featured{background:var(--white);border:2px solid var(--blue)}
.post .cat{font-size:10.5px;color:var(--blue);letter-spacing:.5px}
.post .date{font-size:10.5px;color:#666;margin-top:9px}
.post h3{font-weight:500;font-size:15.5px;line-height:22px;color:var(--ink);margin-top:35px}
.post p{font-size:10.5px;line-height:19px;color:#555;margin-top:10px}
.post .link{position:absolute;left:24px;bottom:38px;font-size:13px;font-weight:500;color:var(--blue);display:flex;align-items:center;gap:10px}

/* footer */
.footer{position:absolute;left:0;top:4933px;width:1200px;height:307px;background:var(--dark);color:var(--white)}
.footer h4{position:absolute;top:30px;font-family:'Oswald',sans-serif;font-weight:500;font-size:17px;color:var(--white)}
.footer .links{position:absolute;left:415px;top:72px;list-style:none;font-size:12px;line-height:26.5px}
.footer .contact{position:absolute;left:563px;top:72px;list-style:none;font-size:12.5px}
.footer .contact li{display:flex;align-items:center;gap:12px;height:39px}
.footer .contact .ic{width:25px;height:25px;border-radius:50%;background:var(--blue);display:flex;align-items:center;justify-content:center}
.footer .brand-box{position:absolute;left:160px;top:97px;width:207px;height:36px;background:var(--white);color:var(--ink);font-weight:600;font-size:21px;display:flex;align-items:center;justify-content:center}
.footer .input{position:absolute;left:791px;top:75px;width:248px;height:37px;background:var(--white);padding:10px 14px;font-size:12px;color:#aaa}
.footer .copy{position:absolute;left:0;top:272px;width:1200px;text-align:center;font-size:12px;color:#ddd}
</style>
</head>
<body>

<!-- Top bar -->
<div class="topbar">
  <span class="social-dot" style="left:157px;top:12px"></span>
  <span class="social-dot" style="left:197px;top:12px"></span>
  <span class="social-dot" style="left:236px;top:12px"></span>
  <div class="info" style="left:658px">
    <svg width="12" height="12" viewBox="0 0 24 24" fill="#fff"><path d="M6.6 10.8a15 15 0 0 0 6.6 6.6l2.2-2.2a1 1 0 0 1 1-.25 11.4 11.4 0 0 0 3.6.57 1 1 0 0 1 1 1V20a1 1 0 0 1-1 1A17 17 0 0 1 3 4a1 1 0 0 1 1-1h3.5a1 1 0 0 1 1 1c0 1.25.2 2.45.57 3.6a1 1 0 0 1-.25 1z"/></svg>
    <span>+1 555 014 2290</span>
  </div>
  <div class="info" style="left:802px">
    <svg width="13" height="11" viewBox="0 0 24 18" fill="#fff"><path d="M0 0h24v18H0z M2 2l10 8 10-8" stroke="#2c5fe4" stroke-width="2"/></svg>
    <span>hello@vantorreach.example</span>
  </div>
</div>

<!-- Navigation -->
<nav class="nav">
  <div class="brand">Vantor Reach</div>
  <a class="active" style="left:400px">HOME</a>
  <a style="left:502px">ABOUT US</a>
  <a style="left:628px">SERVICES</a>
  <a style="left:748px">TEAM</a>
  <a style="left:854px">BLOG</a>
  <a style="left:950px">CONTACT US</a>
</nav>

<!-- Hero -->
<div class="ph hero-photo" role="img" aria-label="Two businessmen in an office reviewing documents on a clipboard, under a deep navy overlay"></div>
<svg class="abs" style="left:0;top:700px" width="1200" height="112" viewBox="0 0 1200 112">
  <path d="M0 62 C400 130 800 100 1200 28 L1200 112 L0 112Z" fill="#1570e6"/>
  <path d="M0 24 C350 92 760 122 1200 62 L1200 112 L0 112Z" fill="#ffffff"/>
</svg>
<h1 class="abs hero-title">Be Found.<br>Be Chosen.</h1>
<p class="abs hero-text">A good strategy is a strategy that can successfully lead the business in a more developed direction and successfully achieve its goals.</p>
<a class="btn" style="left:160px;top:533px;width:138px;height:37px">Learn More</a>

<!-- About -->
<section class="about">
  <div class="abs label" style="left:160px;top:901px">About Us</div>
  <h2 class="abs head" style="left:160px;top:918px;font-size:36px">Who We Are</h2>
  <p style="top:978px">Every pleasure is to be welcomed and every pain avoided. But in certain circumstances and owing to the claims of duty obligations of business it will frequently occur that.</p>
  <p style="top:1076px">If you're able to become pregnant, you should use effective and reliable birth control while taking a GLP-1 agonist. If you become pregnant while taking the immediately.</p>
  <p style="top:1166px">If you're able to become pregnant, you should use effective and reliable birth control while taking a GLP-1 agonist. If you become pregnant while taking the medication, see your healthcare provider immediately.</p>
  <a class="btn" style="left:163px;top:1294px;width:138px;height:35px">Learn More</a>
  <div class="ph" role="img" aria-label="Explainer video still: smiling colleagues at a meeting table" style="left:637px;top:901px;width:403px;height:441px;background:linear-gradient(135deg,#9aa6b8,#5d6f8c 55%,#c9d3e2)"></div>
  <svg class="abs" style="left:820px;top:1086px" width="50" height="50" viewBox="0 0 50 50"><path d="M16 10 L40 25 L16 40Z" fill="#1570e6"/></svg>
  <div class="ph" role="img" aria-label="Two colleagues reviewing notes together" style="left:584px;top:1247px;width:216px;height:171px;border:4px solid #fff;background:linear-gradient(135deg,#b9b4ad,#6e6a66);box-shadow:0 6px 18px rgba(0,0,0,.12)"></div>
</section>

<!-- How we help -->
<svg class="abs" style="left:0;top:1484px" width="1200" height="74" viewBox="0 0 1200 74"><path d="M0 73 L1200 0 L1200 74 L0 74Z" fill="#1570e6"/></svg>
<div class="abs" style="left:0;top:1556px;width:1200px;height:488px;background:var(--dark)"></div>
<h2 class="sec-title" style="top:1606px;color:#fff">How We Help You Succeed</h2>
<p class="sec-sub" style="top:1666px;color:#fff">Together, we help our clients achieve tangible, measurable results.</p>

<div class="help-card" style="left:248px">
  <svg width="50" height="50" viewBox="0 0 50 50" fill="none" stroke="#1570e6" stroke-width="3"><circle cx="22" cy="28" r="19"/><circle cx="22" cy="28" r="11"/><circle cx="22" cy="28" r="3" fill="#1570e6"/><path d="M22 28 L44 6 M38 5 L45 5 L45 12"/></svg>
  <h3>Strategic Frameworks</h3>
  <p>We always provide people a complete solution focused of any business.</p>
  <div class="more"><svg width="22" height="8" viewBox="0 0 22 8"><path d="M0 4H20M16 1l4 3-4 3" stroke="#333" fill="none"/></svg></div>
</div>
<div class="help-card" style="left:490px">
  <svg width="50" height="50" viewBox="0 0 50 50" fill="#1570e6"><rect x="4" y="32" width="6" height="14"/><rect x="14" y="26" width="6" height="20"/><rect x="24" y="20" width="6" height="26"/><path d="M30 16 L44 4" stroke="#1570e6" stroke-width="4"/><path d="M36 2 L47 1 L46 12Z"/></svg>
  <h3>Data-Driven Insights</h3>
  <p>We always provide people a complete solution focused of any business.</p>
  <div class="more"><svg width="22" height="8" viewBox="0 0 22 8"><path d="M0 4H20M16 1l4 3-4 3" stroke="#333" fill="none"/></svg></div>
</div>
<div class="help-card" style="left:730px">
  <svg width="50" height="50" viewBox="0 0 50 50" fill="#1570e6"><rect x="4" y="32" width="7" height="14"/><rect x="15" y="24" width="7" height="22"/><rect x="26" y="28" width="7" height="18"/><rect x="37" y="16" width="7" height="30"/><path d="M4 24 L18 14 L28 20 L44 6" stroke="#1570e6" stroke-width="3" fill="none"/></svg>
  <h3>Growth Acceleration</h3>
  <p>We always provide people a complete solution focused of any business.</p>
  <div class="more">Learn More <svg width="22" height="8" viewBox="0 0 22 8"><path d="M0 4H20M16 1l4 3-4 3" stroke="#333" fill="none"/></svg></div>
</div>

<!-- Services -->
<div class="abs" style="left:0;top:2044px;width:1200px;height:1190px;background:#f6f7f9"></div>
<svg class="abs" style="left:0;top:2044px" width="1200" height="900" viewBox="0 0 1200 900">
  <path d="M0 0 H1200 V60 L0 106Z" fill="#1570e6"/>
  <path d="M0 106 L1200 48 V794 L0 896Z" fill="#262f57"/>
</svg>
<h2 class="sec-title" style="top:2166px;color:#fff">Services We Offer</h2>
<p class="sec-sub" style="top:2224px;color:#fff">There's a low risk of mild low blood sugar hypoglycemia</p>

<div class="ph" role="img" aria-label="Consultants reviewing charts on a laptop" style="left:160px;top:2290px;width:419px;height:277px;background:linear-gradient(135deg,#d9dde3,#7d8696)"></div>
<div class="ph" role="img" aria-label="Smiling team gathered at a meeting table" style="left:620px;top:2290px;width:419px;height:277px;background:linear-gradient(135deg,#c7b9a8,#8a7a6b)"></div>
<div class="svc-box" style="left:179px;top:2506px"><h3>Revenue Intelligence</h3><p>If your prior authorization is denied, the cost of your GLP-1 will not be covered by your insurance, it is important to understand the denial reason.</p><div class="link">Learn More <svg width="18" height="8" viewBox="0 0 18 8"><path d="M0 4H16M12 1l4 3-4 3" stroke="#1570e6" fill="none"/></svg></div></div>
<div class="svc-box" style="left:639px;top:2506px"><h3>Revenue Psychology</h3><p>If your prior authorization is denied, the cost of your GLP-1 will not be covered by your insurance, it is important to understand the denial reason.</p><div class="link">Learn More <svg width="18" height="8" viewBox="0 0 18 8"><path d="M0 4H16M12 1l4 3-4 3" stroke="#1570e6" fill="none"/></svg></div></div>

<div class="ph" role="img" aria-label="Colleagues collaborating around a desk in a bright office" style="left:160px;top:2764px;width:419px;height:279px;background:linear-gradient(135deg,#e4e7ec,#8d97a6)"></div>
<div class="ph" role="img" aria-label="Team celebrating around a laptop" style="left:620px;top:2764px;width:419px;height:279px;background:linear-gradient(135deg,#c6a99a,#6f5a55)"></div>
<div class="svc-box" style="left:179px;top:2982px"><h3>Demand Architecture</h3><p>If your prior authorization is denied, the cost of your GLP-1 will not be covered by your insurance, it is important to understand the denial reason.</p><div class="link">Learn More <svg width="18" height="8" viewBox="0 0 18 8"><path d="M0 4H16M12 1l4 3-4 3" stroke="#1570e6" fill="none"/></svg></div></div>
<div class="svc-box" style="left:639px;top:2982px"><h3>Advisory / Office Hours</h3><p>If your prior authorization is denied, the cost of your GLP-1 will not be covered by your insurance, it is important to understand the denial reason.</p><div class="link">Learn More <svg width="18" height="8" viewBox="0 0 18 8"><path d="M0 4H16M12 1l4 3-4 3" stroke="#1570e6" fill="none"/></svg></div></div>

<!-- Reviews -->
<h2 class="sec-title" style="top:3250px">Customer Review</h2>
<p class="sec-sub" style="top:3310px">There's a low risk of mild low blood sugar hypoglycemia</p>
<svg class="abs" style="left:50px;top:3470px" width="14" height="22" viewBox="0 0 14 22"><path d="M11 2 L3 11 L11 20" stroke="#777" stroke-width="1.5" fill="none"/></svg>
<svg class="abs" style="left:1135px;top:3470px" width="14" height="22" viewBox="0 0 14 22"><path d="M3 2 L11 11 L3 20" stroke="#777" stroke-width="1.5" fill="none"/></svg>

<div class="review" style="left:77px;width:515px">
  <div class="avatar" role="img" aria-label="Client portrait"></div>
  <div class="sign" role="img" aria-label="Handwritten signature"></div>
  <div class="stars">★★★★★</div>
  <div class="quote">”</div>
  <div class="name">Marcus Hale – <b>Broker Partner</b></div>
  <p>Ellie is one of a kind. She has been a key partner to our business and has run the extra mile to ensure our clients are looked after. I highly recommend her for any non-conforming lending scenarios.</p>
</div>
<div class="review" style="left:608px;width:513px">
  <div class="avatar" role="img" aria-label="Client portrait"></div>
  <div class="sign" role="img" aria-label="Handwritten signature"></div>
  <div class="stars">★★★★★</div>
  <div class="quote">”</div>
  <div class="name">Marcus Hale – <b>Broker Partner</b></div>
  <p>Ellie is one of a kind. She has been a key partner to our business and has run the extra mile to ensure our clients are looked after. I highly recommend her for any non-conforming lending scenarios.</p>
</div>
<div class="abs" style="left:572px;top:3634px;display:flex;gap:5px;align-items:center">
  <span style="width:7px;height:7px;border-radius:50%;background:#c9ccd3"></span>
  <span style="width:7px;height:7px;border-radius:50%;background:#c9ccd3"></span>
  <span style="width:7px;height:7px;border-radius:50%;background:#c9ccd3"></span>
  <span style="width:20px;height:7px;border-radius:4px;background:var(--blue)"></span>
</div>

<!-- Team -->
<div class="abs" style="left:0;top:3702px;width:1200px;height:549px;background:var(--light)"></div>
<h2 class="sec-title" style="top:3740px">Our Team</h2>
<p class="sec-sub" style="top:3798px">There's a low risk of mild low blood sugar hypoglycemia</p>
<div class="member" role="img" aria-label="Team member portrait" style="left:163px"><div class="tag">Elena Marsh</div></div>
<div class="member" role="img" aria-label="Team member portrait" style="left:387px"><div class="tag">Owen Carter</div></div>
<div class="member" role="img" aria-label="Team member portrait" style="left:612px"><div class="tag">Clara Reyes</div></div>
<div class="member" role="img" aria-label="Team member portrait" style="left:838px"><div class="tag">Daniel Brooks</div></div>
<a class="btn" style="left:523px;top:4162px;width:155px;height:37px">View All Member</a>

<!-- Blog -->
<h2 class="sec-title" style="top:4294px">Latest Blog</h2>
<article class="post" style="left:163px">
  <div class="cat">VANTOR REACH</div><div class="date">jan 25, 2026</div>
  <h3>5 Surprising Benefits of Naturopathic Mud Therapy...</h3>
  <p>Consectetuer fringilla aenean sagittis potenti ullamcorper nam porta feugiat. Ante urna congue feugiat efficitur vel duis.</p>
  <div class="link">Continue Reading <svg width="18" height="8" viewBox="0 0 18 8"><path d="M0 4H16M12 1l4 3-4 3" stroke="#1570e6" fill="none"/></svg></div>
</article>
<article class="post" style="left:462px">
  <div class="cat">VANTOR REACH</div><div class="date">jan 25, 2026</div>
  <h3>Exploring the Profound Benefits of Jal Neti...</h3>
  <p>Consectetuer fringilla aenean sagittis potenti ullamcorper nam porta feugiat. Ante urna congue feugiat efficitur vel duis.</p>
  <div class="link">Continue Reading <svg width="18" height="8" viewBox="0 0 18 8"><path d="M0 4H16M12 1l4 3-4 3" stroke="#1570e6" fill="none"/></svg></div>
</article>
<article class="post featured" style="left:761px">
  <div class="cat">VANTOR REACH</div><div class="date">jan 25, 2026</div>
  <h3>Mastering the Art of Overcoming Junk Food...</h3>
  <p>Consectetuer fringilla aenean sagittis potenti ullamcorper nam porta feugiat. Ante urna congue feugiat efficitur vel duis.</p>
  <div class="link">Continue Reading <svg width="18" height="8" viewBox="0 0 18 8"><path d="M0 4H16M12 1l4 3-4 3" stroke="#1570e6" fill="none"/></svg></div>
</article>
<a class="btn" style="left:531px;top:4760px;width:138px;height:37px">View All Blog</a>

<!-- Footer -->
<svg class="abs" style="left:0;top:4858px" width="1200" height="80" viewBox="0 0 1200 80">
  <path d="M0 70 C300 30 700 -10 1200 40 L1200 80 L0 80Z" fill="#1570e6"/>
  <path d="M0 80 C350 48 760 30 1200 60 L1200 80Z" fill="#2b2b2b"/>
</svg>
<footer class="footer">
  <div class="brand-box">Vantor Reach</div>
  <span class="social-dot" style="left:212px;top:158px"></span>
  <span class="social-dot" style="left:256px;top:158px"></span>
  <span class="social-dot" style="left:298px;top:158px"></span>

  <h4 style="left:415px">Quick Links</h4>
  <ul class="links"><li>Home</li><li>About Us</li><li>Services</li><li>Team</li><li>Blog</li><li>Contact Us</li></ul>

  <h4 style="left:563px">Contact Us</h4>
  <ul class="contact">
    <li><span class="ic"><svg width="11" height="11" viewBox="0 0 24 24" fill="#fff"><path d="M6.6 10.8a15 15 0 0 0 6.6 6.6l2.2-2.2a1 1 0 0 1 1-.25 11.4 11.4 0 0 0 3.6.57 1 1 0 0 1 1 1V20a1 1 0 0 1-1 1A17 17 0 0 1 3 4a1 1 0 0 1 1-1h3.5a1 1 0 0 1 1 1c0 1.25.2 2.45.57 3.6a1 1 0 0 1-.25 1z"/></svg></span>+1 555 014 2290</li>
    <li><span class="ic"><svg width="12" height="9" viewBox="0 0 24 18"><rect width="24" height="18" fill="#fff"/><path d="M1 1l11 9 11-9" stroke="#1570e6" stroke-width="2" fill="none"/></svg></span>team@vantorreach.example</li>
    <li><span class="ic"><svg width="10" height="13" viewBox="0 0 20 26" fill="#fff"><path d="M10 0a10 10 0 0 1 10 10c0 7-10 16-10 16S0 17 0 10A10 10 0 0 1 10 0z"/><circle cx="10" cy="10" r="4" fill="#1570e6"/></svg></span>122, Lorem ipsum dolrd</li>
  </ul>

  <h4 style="left:791px">Subscribe To Our Newsletter</h4>
  <div class="input">E-mail</div>
  <a class="btn" style="left:791px;top:122px;width:101px;height:35px;font-size:11px;font-weight:600">SUBSCRIBE</a>

  <div class="copy">Copyright © 2026 Vantor Reach Consulting - All Rights Reserved.</div>
</footer>

</body>
</html>
```